MODERN DESIGN BUSINESS CARDS FOR A CREDIT REPAIR COMPANY

Our goal is to have a modern yet professional business card for our credit repair company. Something that'll catch the eye of our clients. PLEASE BE CREATIVE. WE WOULD LIKE TO SEE HOW THIS WOULD LOOK WITH A WHITE AND BLACK BACK GROUND.

Contact Information for Business Card

THIS WILL BE A DOUBLE SIDED BUSINESS CARD, THE COLORS WE WOULD LIKE TO HAVE IS BLACK, BLUES AND WHITE

Colors
3277b5
33a6d7
ffffff

Requirements
Must have
• MUST HAVE OUR LOGO, BUSINESS PHONE # (956 )482-7153, FACEBOOK LINK FACEBOOK.COM/VORMANTEKCREDITSOLUTIONS, CALL US FOR YOUR FREE CONSULTATION
Nice to have
• ITEMS WE DELETE: LATE PAYMENTS, CHARGE-OFFS, REPOSESSIONS, HOSPITAL BILLS, STUDENT LOANS, FORECLOSURES, CHILD SUPPORT AND BANKRUPTCIES.

```html
<!DOCTYPE html>
<html lang="en">
<head>
<meta charset="utf-8">
<title>Vormantek Credit Solutions – Business Cards</title>
<link rel="stylesheet" href="https://fonts.googleapis.com/css2?family=Arimo:wght@400;700&family=Lato:wght@400;700&family=Montserrat:wght@600&display=swap">
<style>
  :root {
    --page: #e6e4e5;
    --frost-top: #f4f2f2;
    --frost-bottom: #e7e3e3;
    --navy: #0f3e7a;
    --charcoal: #454547;
    --strip-dark: #3d3d3f;
    --white: #ffffff;
    --logo-navy: #1b4b8c;
    --faint: #b9bcc2;
    --rule: #6d86ad;
  }
  * { box-sizing: border-box; margin: 0; padding: 0; }
  html, body { width: 1200px; height: 1181px; overflow: hidden; }
  body { background: var(--page); position: relative; font-family: "Arimo", Arial, sans-serif; }

  .card {
    position: absolute;
    width: 654px;
    height: 403px;
    overflow: hidden;
    box-shadow: 0 6px 18px rgba(0,0,0,0.12);
  }
  .card-front { left: 181px; top: 156px; }
  .card-back  { left: 480px; top: 627px; }

  .frost {
    position: absolute; left: 0; top: 0; width: 100%; height: 197px;
    background: linear-gradient(180deg, var(--frost-top), var(--frost-bottom));
  }

  /* Front */
  .brand {
    position: absolute; left: 0; top: 0; width: 100%; height: 197px;
    display: flex; align-items: center; justify-content: center; gap: 16px;
  }
  .brand-dot { width: 34px; height: 34px; border-radius: 50%; background: var(--logo-navy); }
  .brand-name {
    font-family: "Montserrat", sans-serif; font-weight: 600;
    font-size: 46px; letter-spacing: 1px; color: var(--logo-navy);
  }
  .front-strip { position: absolute; left: 0; top: 197px; width: 100%; height: 6px; background: var(--strip-dark); }
  .front-panel {
    position: absolute; left: 0; top: 203px; width: 100%; height: 200px;
    background: var(--navy); color: var(--white); text-align: center;
  }
  .phone { position: absolute; left: 0; width: 100%; top: 18px; font-size: 27px; font-weight: 700; }
  .cta { position: absolute; left: 0; width: 100%; top: 59px; font-size: 19.5px; }
  .social-row { position: absolute; left: 102px; width: 450px; top: 104px; height: 36px; }
  .social-row .rule { position: absolute; top: 18px; height: 1px; width: 199px; background: var(--rule); }
  .social-row .rule.left { left: 0; }
  .social-row .rule.right { right: 0; }
  .social-row .mark { position: absolute; left: 209px; top: 2px; width: 32px; height: 32px; border-radius: 50%; background: var(--white); }
  .url { position: absolute; left: 0; width: 100%; top: 147px; font-size: 19.5px; }

  /* Back */
  .faint-name {
    position: absolute; left: 0; top: 0; width: 100%; height: 198px;
    display: flex; align-items: center; justify-content: center;
    font-family: "Montserrat", sans-serif; font-weight: 600; font-size: 44px;
    letter-spacing: 1px; color: var(--faint); opacity: 0.75;
  }
  .back-strip { position: absolute; left: 0; top: 198px; width: 100%; height: 7px; background: var(--navy); }
  .back-panel {
    position: absolute; left: 0; top: 205px; width: 100%; height: 198px;
    background: var(--charcoal); color: var(--white); font-family: "Lato", sans-serif;
  }
  .items-title { position: absolute; left: 39px; top: 17px; font-size: 24px; font-weight: 700; }
  .items-list { position: absolute; top: 64px; list-style: none; }
  .items-list.col-1 { left: 39px; }
  .items-list.col-2 { left: 238px; }
  .items-list li { position: relative; padding-left: 16px; height: 27.7px; font-size: 19.5px; line-height: 24px; }
  .items-list li::before {
    content: ""; position: absolute; left: 1px; top: 7px; width: 10px; height: 10px;
    border-radius: 50%; background: var(--white);
  }
  .divider { position: absolute; left: 442px; top: 68px; width: 2px; height: 100px; background: var(--white); }
  .cert-seal { position: absolute; left: 470px; top: 41px; width: 142px; height: 142px; }
</style>
</head>
<body>

<section class="card card-front" aria-label="Business card front">
  <div class="frost"></div>
  <div class="brand">
    <span class="brand-dot"></span>
    <span class="brand-name">VORMANTEK</span>
  </div>
  <div class="front-strip"></div>
  <div class="front-panel">
    <p class="phone">(956 )482-7153</p>
    <p class="cta">CALL US FOR YOUR FREE CONSULTATION</p>
    <div class="social-row">
      <span class="rule left"></span>
      <span class="mark"></span>
      <span class="rule right"></span>
    </div>
    <p class="url">PALSPACE.COM/VORMANTEKCREDITSOLUTIONS</p>
  </div>
</section>

<section class="card card-back" aria-label="Business card back">
  <div class="frost" style="height:198px"></div>
  <div class="faint-name">VORMANTEK</div>
  <div class="back-strip"></div>
  <div class="back-panel">
    <h2 class="items-title">ITEMS WE DELETE</h2>
    <ul class="items-list col-1">
      <li>LATE PAYMENTS</li>
      <li>CHARGE-OFFS</li>
      <li>REPOSESSIONS</li>
      <li>HOSPITAL BILLS</li>
    </ul>
    <ul class="items-list col-2">
      <li>STUDENT LOANS</li>
      <li>FORECLOSURES</li>
      <li>CHILD SUPPORT</li>
      <li>BANKRUPTCIES</li>
    </ul>
    <span class="divider"></span>
    <svg class="cert-seal" viewBox="0 0 142 142" role="img" aria-label="Certification seal">
      <circle cx="71" cy="71" r="62" fill="#1d4f9c"/>
    </svg>
  </div>
</section>

</body>
</html>
```